FinTech company looking to revamp and expand client-facing interface for our financial models

Halvern Ledgerworks currently has a very simple website that allows clients to interact with our financial models. We are looking to completely redesign the current site and add several extra pages to provide extra functionality. We want the design to have a modern, slick feel, that will work on both a desktop or a tablet. It should be straightforward for clients to move between different pages at any time, and clear from the layout how to interact with the more advanced features. We have included screenshots of existing pages in the attached design brief, as well as sketches of the functionality required by the new pages, but can't provide a direct link to the current site.
Target Market(s)
Professional investors that will be paying to access the interface
Industry/Entity Type
Finance
Number of Pages Required
4 page
Colors
Designer to choose colors to be used in the design.
Look and feel
Each slider illustrates characteristics of the customer's brand and the style your logo design should communicate.

```html
<!DOCTYPE html>
<html lang="en">
<head>
<meta charset="utf-8">
<title>Halvern Ledgerworks – Sensitivities</title>
<link href="https://fonts.googleapis.com/css2?family=Lato:wght@300;400;700;900&display=swap" rel="stylesheet">
<style>
  :root{
    --navy:#0d1b30;
    --navy-band:#0f2542;
    --red:#d7263d;
    --blue:#1e90e8;
    --input-blue:#3a9ff0;
    --row-blue:#eef6f9;
    --row-pink:#fdf0f2;
    --ink:#1d2a3a;
    --text:#454c55;
    --muted:#c3ccd8;
    --rule:#d9dde2;
    --star:#f29222;
  }
  *{box-sizing:border-box;margin:0;padding:0}
  html,body{width:693px;height:1200px;overflow:hidden;background:#fff}
  body{font-family:'Lato',sans-serif}
  .canvas{width:693px;height:1200px;overflow:hidden;position:relative}
  .stage{width:1366px;height:2365px;position:relative;transform:scale(.50732);transform-origin:0 0}
  .screen{position:absolute;left:0;width:1366px}
  .screen--one{top:0;height:971px}
  .screen--two{top:971px;height:1394px}

  .sidebar{position:absolute;left:0;top:0;width:316px;height:100%;background:var(--navy);color:#fff}
  .brand{position:absolute;top:26px;width:100%;text-align:center;font-size:40px;font-weight:300;letter-spacing:1px;color:#fff}
  .brand::before{content:"";display:inline-block;width:12px;height:12px;border-radius:50%;background:var(--blue);margin-right:10px;vertical-align:middle}
  .user{position:absolute;top:100px;width:100%;height:56px;background:var(--navy-band);display:flex;align-items:center;padding-left:59px;font-size:16px;font-weight:700}
  .avatar{width:40px;height:40px;border-radius:50%;background:linear-gradient(135deg,#8f86e8,#f0a39a);margin-right:11px}
  .nav{position:absolute;top:172px;width:100%;list-style:none}
  .nav li{height:43px;display:flex;align-items:center;justify-content:space-between;padding:0 66px 0 58px;font-size:16px}
  .nav .group{font-weight:900}
  .nav .sub{color:var(--muted);font-weight:400;font-size:17px}
  .nav .active{background:var(--red);color:#fff;font-weight:400;font-size:17px;height:40px}
  .collapse{position:absolute;left:316px;top:27px;width:40px;height:38px;background:var(--navy);border-radius:0 19px 19px 0;display:flex;align-items:center;justify-content:center}

  .page-title{position:absolute;left:387px;top:44px;font-size:29px;font-weight:400;color:var(--ink);letter-spacing:.5px}
  .title-rule{position:absolute;left:326px;top:87px;width:954px;height:2px;background:var(--rule)}
  .thresholds{position:absolute;left:387px;top:118px}
  .threshold{display:flex;align-items:center;height:28px;margin-bottom:31px;font-size:16px;color:var(--ink)}
  .threshold .stat{width:72px}
  .threshold .label{width:82px}
  .threshold .field{width:162px;height:27px;border:1.5px solid var(--input-blue);border-radius:4px}
  .thresh-rule{position:absolute;left:353px;top:300px;width:398px;height:1.5px;background:var(--rule)}
  .filter-btn{position:absolute;left:392px;top:333px;width:119px;height:39px;background:var(--red);color:#fff;font-size:16px;display:flex;align-items:center;justify-content:center;gap:10px;border-radius:2px}

  .filter-panel{position:absolute;left:393px;top:373px;width:839px;height:319px;background:var(--row-pink);border:1px solid #bfc3c8;display:grid;grid-auto-flow:column;grid-template-rows:repeat(10,32px);grid-template-columns:repeat(5,170px);padding-left:41px}
  .option{display:flex;align-items:center;font-size:13px;color:var(--text);gap:9px}
  .box{width:13px;height:13px;border:1px solid #8d9196;background:#fff;display:flex;align-items:center;justify-content:center}

  .results{position:absolute;left:391px}
  .screen--one .results{top:398px}
  .screen--two .results{top:720px}
  .export{display:flex;align-items:center;gap:10px;font-size:19px;color:var(--red);height:30px}
  .tabs{position:absolute;top:48px;left:0;display:flex;align-items:flex-end}
  .tab{height:40px;width:87px;background:var(--navy);color:#fff;font-size:13px;display:flex;align-items:center;justify-content:center;border-radius:6px 6px 0 0;margin-right:17px}
  .tab--active{background:var(--blue);margin-right:13px;position:relative}
  .tab--active::after{content:"";position:absolute;bottom:1px;left:24px;width:40px;height:1.5px;background:#fff}
  .tab-add{margin-left:8px;margin-bottom:8px}
  .table{position:absolute;top:88px;left:0;width:839px;border:1px solid #bfc3c8;border-top:none}
  .row{display:grid;grid-template-columns:18px 100px 81px 162px 28px 74px 74px 73px 71px 76px 74px 1fr;align-items:center;height:63.5px;font-size:12px;color:var(--text);position:relative}
  .row span{text-align:center}
  .row span.left{text-align:left}
  .row:nth-child(odd){background:var(--row-pink)}
  .row:nth-child(even){background:var(--row-blue)}
  .head{height:47px;background:var(--blue)!important;color:#fff;font-weight:700;font-size:13.5px}
  .more{position:absolute;left:839px;top:0;width:54px;height:47px;background:var(--red);color:#fff;font-size:12.5px;display:flex;align-items:center;justify-content:center}
  .star{position:absolute;left:-33px;top:14px}
</style>
</head>
<body>
<div class="canvas">
<div class="stage">

  <!-- First state: filter closed -->
  <section class="screen screen--one">
    <aside class="sidebar">
      <div class="brand">LEDGRA</div>
      <div class="user"><div class="avatar" role="img" aria-label="User avatar"></div>Username</div>
      <ul class="nav">
        <li class="group">250D <svg width="18" height="10"><path d="M1 1l8 8 8-8" fill="none" stroke="#fff" stroke-width="1.6"/></svg></li>
        <li class="sub">MODELS</li>
        <li class="active">SENSETIVITIES</li>
        <li class="group">42D <svg width="10" height="18"><path d="M1 1l8 8-8 8" fill="none" stroke="#fff" stroke-width="1.6"/></svg></li>
        <li class="group">83D <svg width="10" height="18"><path d="M1 1l8 8-8 8" fill="none" stroke="#fff" stroke-width="1.6"/></svg></li>
      </ul>
    </aside>
    <div class="collapse"><svg width="14" height="20"><path d="M12 1L2 10l10 9" fill="none" stroke="#fff" stroke-width="2"/></svg></div>

    <h1 class="page-title">SENSITIVITIES</h1>
    <div class="title-rule"></div>
    <div class="thresholds">
      <div class="threshold"><span class="stat">Stat 1</span><span class="label">Threshold :</span><span class="field"></span></div>
      <div class="threshold"><span class="stat">Stat 2</span><span class="label">Threshold :</span><span class="field"></span></div>
      <div class="threshold"><span class="stat">Stat 1</span><span class="label">Threshold :</span><span class="field"></span></div>
    </div>
    <div class="thresh-rule"></div>
    <div class="filter-btn">FILTER <svg width="16" height="13"><path d="M0 1.5h16M0 6.5h16M0 11.5h16" stroke="#fff" stroke-width="2.4"/></svg></div>

    <div class="results">
      <div class="export"><svg width="20" height="18"><path d="M8 4H1v13h14v-6" fill="none" stroke="#555" stroke-width="1.4"/><path d="M6 12c1-5 5-7 10-7M13 2l4 3-4 3" fill="none" stroke="#555" stroke-width="1.4"/></svg>Export</div>
      <div class="tabs">
        <div class="tab tab--active">EQUITIES</div><div class="tab">EFTS</div><div class="tab">EFT PAIRS</div><div class="tab">PAIRS</div>
        <svg class="tab-add" width="20" height="20"><path d="M10 0v20M0 10h20" stroke="#1e90e8" stroke-width="3.4"/></svg>
      </div>
      <div class="table">
        <div class="more">More</div>
        <div class="row head"><span></span><span class="left">FACTOR</span><span class="left">ID ⌵</span><span>SECTOR</span><span></span><span>Stat 1</span><span>Stat 2</span><span>Stat 3</span><span>Stat 4</span><span>Stat 5</span><span>Stat 6</span><span></span></div>
        <div class="row"><svg class="star" width="30" height="32"><path d="M11 8l3 6.5 7 .8-5.2 4.8 1.4 7L11 23.5 4.8 27l1.4-7L1 15.3l7-.8z" fill="#f29222"/><path d="M22 0v11M16.5 5.5h11" stroke="#1e90e8" stroke-width="2.6"/></svg><span></span><span class="left">Factor 1</span><span class="left">Model 1</span><span>Materials</span><span></span><span>-1.4</span><span>0.1</span><span>-3.1</span><span>0.7</span><span>30.2</span><span>0.9</span><span></span></div>
        <div class="row"><svg class="star" width="30" height="32"><path d="M11 8l3 6.5 7 .8-5.2 4.8 1.4 7L11 23.5 4.8 27l1.4-7L1 15.3l7-.8z" fill="#f29222"/><path d="M22 0v11M16.5 5.5h11" stroke="#1e90e8" stroke-width="2.6"/></svg><span></span><span class="left">Factor 2</span><span class="left">Model 2</span><span>Materials</span><span></span><span>2.8</span><span>0.1</span><span>6.1</span><span>100</span><span>30.2</span><span>0.9</span><span></span></div>
        <div class="row"><svg class="star" width="30" height="32"><path d="M11 8l3 6.5 7 .8-5.2 4.8 1.4 7L11 23.5 4.8 27l1.4-7L1 15.3l7-.8z" fill="#f29222"/><path d="M22 0v11M16.5 5.5h11" stroke="#1e90e8" stroke-width="2.6"/></svg><span></span><span class="left">Factor 3</span><span class="left">Model 3</span><span>Materials</span><span></span><span>-3.7</span><span>2.7</span><span>-7.2</span><span>100</span><span>30.2</span><span>0.9</span><span></span></div>
        <div class="row"><svg class="star" width="30" height="32"><path d="M11 8l3 6.5 7 .8-5.2 4.8 1.4 7L11 23.5 4.8 27l1.4-7L1 15.3l7-.8z" fill="#f29222"/><path d="M22 0v11M16.5 5.5h11" stroke="#1e90e8" stroke-width="2.6"/></svg><span></span><span class="left">Factor 4</span><span class="left">Model 4</span><span>Materials</span><span></span><span>2.8</span><span>0.2</span><span>2.7</span><span>0.5</span><span>32.9</span><span>-0.5</span><span></span></div>
        <div class="row"><svg class="star" width="30" height="32"><path d="M11 8l3 6.5 7 .8-5.2 4.8 1.4 7L11 23.5 4.8 27l1.4-7L1 15.3l7-.8z" fill="#f29222"/><path d="M22 0v11M16.5 5.5h11" stroke="#1e90e8" stroke-width="2.6"/></svg><span></span><span class="left">Factor 5</span><span class="left">Model 5</span><span>Materials</span><span></span><span>0.8</span><span>0.3</span><span>2.5</span><span>0.5</span><span>32.9</span><span>-0.5</span><span></span></div>
      </div>
    </div>
  </section>

  <!-- Second state: filter open -->
  <section class="screen screen--two">
    <aside class="sidebar">
      <div class="brand">LEDGRA</div>
      <div class="user"><div class="avatar" role="img" aria-label="User avatar"></div>Username</div>
      <ul class="nav">
        <li class="group">250D <svg width="18" height="10"><path d="M1 1l8 8 8-8" fill="none" stroke="#fff" stroke-width="1.6"/></svg></li>
        <li class="sub">MODELS</li>
        <li class="active">SENSETIVES</li>
        <li class="group">42D <svg width="10" height="18"><path d="M1 1l8 8-8 8" fill="none" stroke="#fff" stroke-width="1.6"/></svg></li>
        <li class="group">83D <svg width="10" height="18"><path d="M1 1l8 8-8 8" fill="none" stroke="#fff" stroke-width="1.6"/></svg></li>
      </ul>
    </aside>
    <div class="collapse"><svg width="14" height="20"><path d="M12 1L2 10l10 9" fill="none" stroke="#fff" stroke-width="2"/></svg></div>

    <h1 class="page-title">SENSITIVES</h1>
    <div class="title-rule"></div>
    <div class="thresholds">
      <div class="threshold"><span class="stat">Stat 1</span><span class="label">Threshold :</span><span class="field"></span></div>
      <div class="threshold"><span class="stat">Stat 2</span><span class="label">Threshold :</span><span class="field"></span></div>
      <div class="threshold"><span class="stat">Stat 1</span><span class="label">Threshold :</span><span class="field"></span></div>
    </div>
    <div class="thresh-rule"></div>
    <div class="filter-btn">FILTER <svg width="16" height="13"><path d="M0 1.5h16M0 6.5h16M0 11.5h16" stroke="#fff" stroke-width="2.4"/></svg></div>

    <div class="filter-panel">
      <label class="option"><span class="box"><svg width="11" height="11"><path d="M1 6l3 3 6-8" fill="none" stroke="#555" stroke-width="1.3"/></svg></span>Factor 1</label>
      <label class="option"><span class="box"></span>Factor 2</label><label class="option"><span class="box"></span>Factor 3</label><label class="option"><span class="box"></span>Factor 4</label><label class="option"><span class="box"></span>Factor 5</label><label class="option"><span class="box"></span>Factor 6</label><label class="option"><span class="box"></span>Factor 7</label><label class="option"><span class="box"></span>Factor 8</label><label class="option"><span class="box"></span>Factor 9</label><label class="option"><span class="box"></span>Factor 10</label>
      <label class="option"><span class="box"></span>Factor 11</label><label class="option"><span class="box"></span>Factor 12</label><label class="option"><span class="box"></span>Factor 13</label><label class="option"><span class="box"></span>Factor 14</label><label class="option"><span class="box"></span>Factor 15</label><label class="option"><span class="box"></span>Factor 16</label><label class="option"><span class="box"></span>Factor 17</label><label class="option"><span class="box"></span>Factor 18</label><label class="option"><span class="box"></span>Factor 19</label><label class="option"><span class="box"></span>Factor 20</label>
      <label class="option"><span class="box"></span>Factor 21</label><label class="option"><span class="box"></span>Factor 22</label><label class="option"><span class="box"></span>Factor 23</label><label class="option"><span class="box"></span>Factor 24</label><label class="option"><span class="box"></span>Factor 25</label><label class="option"><span class="box"></span>Factor 26</label><label class="option"><span class="box"></span>Factor 27</label><label class="option"><span class="box"></span>Factor 28</label><label class="option"><span class="box"></span>Factor 29</label><label class="option"><span class="box"></span>Factor 30</label>
      <label class="option"><span class="box"></span>Factor 31</label><label class="option"><span class="box"></span>Factor 32</label><label class="option"><span class="box"></span>Factor 33</label><label class="option"><span class="box"></span>Factor 34</label><label class="option"><span class="box"></span>Factor 35</label><label class="option"><span class="box"></span>Factor 36</label><label class="option"><span class="box"></span>Factor 37</label><label class="option"><span class="box"></span>Factor 38</label><label class="option"><span class="box"></span>Factor 39</label><label class="option"><span class="box"></span>Factor 40</label>
      <label class="option"><span class="box"></span>Factor 41</label><label class="option"><span class="box"></span>Factor 42</label><label class="option"><span class="box"></span>Factor 43</label><label class="option"><span class="box"></span>Factor 44</label><label class="option"><span class="box"></span>Factor 45</label><label class="option"><span class="box"></span>Factor 46</label><label class="option"><span class="box"></span>Factor 47</label><label class="option"><span class="box"></span>Factor 48</label><label class="option"><span class="box"></span>Factor 49</label><label class="option"><span class="box"></span>Factor 50</label>
    </div>

    <div class="results">
      <div class="export"><svg width="20" height="18"><path d="M8 4H1v13h14v-6" fill="none" stroke="#555" stroke-width="1.4"/><path d="M6 12c1-5 5-7 10-7M13 2l4 3-4 3" fill="none" stroke="#555" stroke-width="1.4"/></svg>Export</div>
      <div class="tabs">
        <div class="tab tab--active">EQUITIES</div><div class="tab">EFTS</div><div class="tab">EFT PAIRS</div><div class="tab">PAIRS</div>
        <svg class="tab-add" width="20" height="20"><path d="M10 0v20M0 10h20" stroke="#1e90e8" stroke-width="3.4"/></svg>
      </div>
      <div class="table">
        <div class="more">More</div>
        <div class="row head"><span></span><span class="left">FACTOR</span><span class="left">ID ⌵</span><span>SECTOR</span><span></span><span>Stat 1</span><span>Stat 2</span><span>Stat 3</span><span>Stat 4</span><span>Stat 5</span><span>Stat 6</span><span></span></div>
        <div class="row"><svg class="star" width="30" height="32"><path d="M11 8l3 6.5 7 .8-5.2 4.8 1.4 7L11 23.5 4.8 27l1.4-7L1 15.3l7-.8z" fill="#f29222"/><path d="M22 0v11M16.5 5.5h11" stroke="#1e90e8" stroke-width="2.6"/></svg><span></span><span class="left">Factor 1</span><span class="left">Model 1</span><span>Materials</span><span></span><span>-1.4</span><span>0.1</span><span>-3.1</span><span>0.7</span><span>30.2</span><span>0.9</span><span></span></div>
        <div class="row"><svg class="star" width="30" height="32"><path d="M11 8l3 6.5 7 .8-5.2 4.8 1.4 7L11 23.5 4.8 27l1.4-7L1 15.3l7-.8z" fill="#f29222"/><path d="M22 0v11M16.5 5.5h11" stroke="#1e90e8" stroke-width="2.6"/></svg><span></span><span class="left">Factor 2</span><span class="left">Model 2</span><span>Materials</span><span></span><span>2.8</span><span>0.1</span><span>6.1</span><span>100</span><span>30.2</span><span>0.9</span><span></span></div>
        <div class="row"><svg class="star" width="30" height="32"><path d="M11 8l3 6.5 7 .8-5.2 4.8 1.4 7L11 23.5 4.8 27l1.4-7L1 15.3l7-.8z" fill="#f29222"/><path d="M22 0v11M16.5 5.5h11" stroke="#1e90e8" stroke-width="2.6"/></svg><span></span><span class="left">Factor 3</span><span class="left">Model 3</span><span>Materials</span><span></span><span>-3.7</span><span>2.7</span><span>-7.2</span><span>100</span><span>30.2</span><span>0.9</span><span></span></div>
        <div class="row"><svg class="star" width="30" height="32"><path d="M11 8l3 6.5 7 .8-5.2 4.8 1.4 7L11 23.5 4.8 27l1.4-7L1 15.3l7-.8z" fill="#f29222"/><path d="M22 0v11M16.5 5.5h11" stroke="#1e90e8" stroke-width="2.6"/></svg><span></span><span class="left">Factor 4</span><span class="left">Model 4</span><span>Materials</span><span></span><span>2.8</span><span>0.2</span><span>2.7</span><span>0.5</span><span>32.9</span><span>-0.5</span><span></span></div>
        <div class="row"><svg class="star" width="30" height="32"><path d="M11 8l3 6.5 7 .8-5.2 4.8 1.4 7L11 23.5 4.8 27l1.4-7L1 15.3l7-.8z" fill="#f29222"/><path d="M22 0v11M16.5 5.5h11" stroke="#1e90e8" stroke-width="2.6"/></svg><span></span><span class="left">Factor 5</span><span class="left">Model 5</span><span>Materials</span><span></span><span>0.8</span><span>0.3</span><span>2.5</span><span>0.5</span><span>32.9</span><span>-0.5</span><span></span></div>
      </div>
    </div>
  </section>

</div>
</div>
</body>
</html>
```